Web design concept for a IT recruitment agency.

Our website addresses two different target groups:
- Customers (companies) wanting to hire new IT talent
- It talent to find a new JOB

We a looking for a visual design concept that either addresses both target groups in one of the following options:
a. target both groups in 1 single splash page.
b. target both groups in 2 different pages one for both groups
c. or any creative third concept you can come up with

Requirements, we want one overall visual concept, that both target groups can relate to.

Trigger words what we want to express:
- passion / drive
- knowhow
- involvement
- professional/yet playful
- engagement

Background, company culture:
We are a recruitment agency with over 15 years of experience, we have no hard-sale culture.
But we emphasize on long term relationships, showing real interest in people and their needs.

Design requirements:
Use logo
Flat contemporary design

Target Market(s)

Industry/Entity Type

Hire

Number of Pages Required

2 page

Requirements
Must have
• We a looking for a visual design concept that either addresses both target groups

```html
<!DOCTYPE html>
<html lang="en">
<head>
<meta charset="utf-8">
<title>Brightline Talent – IT Recruitment</title>
<link rel="stylesheet" href="https://fonts.googleapis.com/css2?family=Open+Sans:ital,wght@0,400;0,600;0,700;0,800;1,700&display=swap">
<style>
:root{
  --blue:#1fa3e0;
  --blue-dark:#1687bd;
  --ink:#333b42;
  --grey-text:#6d7278;
  --light:#f4f5f6;
  --dark:#2c2f33;
  --footer:#3a3c3f;
  --white:#ffffff;
}
*{margin:0;padding:0;box-sizing:border-box}
html,body{width:1200px;height:2548px;overflow:hidden;background:var(--white)}
body{font-family:"Open Sans",Arial,sans-serif;color:var(--ink);position:relative}
section,header,footer{position:absolute;left:0;width:1200px}

/* header */
.site-header{top:0;height:140px;background:var(--white)}
.brand{position:absolute;left:70px;top:34px;display:flex;align-items:center;gap:14px}
.brand-dot{width:44px;height:44px;border-radius:50%;background:var(--blue)}
.brand-name{font-size:30px;font-weight:700;color:var(--blue-dark);line-height:1}
.contact-bar{position:absolute;right:70px;top:20px;display:flex;gap:30px;font-size:13px;color:var(--ink)}
.contact-bar span{display:flex;align-items:center;gap:6px}
.main-nav{position:absolute;right:70px;top:92px;display:flex;gap:44px;font-size:13px;font-weight:600;text-transform:uppercase;color:var(--ink)}

/* hero */
.hero{top:140px;height:580px;background:linear-gradient(90deg,#d9dde0 0%,#b9bfc4 45%,#6f767c 75%,#4a4f54 100%)}
.hero-photo{position:absolute;left:0;top:0;width:640px;height:580px;background:radial-gradient(ellipse at 45% 45%,#c9cdd1 0%,#a8aeb3 60%,#8e9499 100%)}
.hero-copy{position:absolute;left:540px;top:250px;width:620px}
.hero-title{font-size:46px;font-weight:800;color:var(--blue);letter-spacing:1px;background:rgba(255,255,255,.1)}
.hero-sub{margin-top:18px;font-size:40px;font-style:italic;font-weight:700;color:var(--white);line-height:1.3;letter-spacing:1px}
.hero-next{position:absolute;right:34px;top:258px}

/* about */
.about{top:720px;height:320px;background:var(--white);text-align:center}
.section-title{font-size:20px;font-weight:700;text-transform:uppercase;color:var(--ink)}
.section-title em{font-style:normal;color:var(--blue)}
.about .section-title{margin-top:60px}
.about p{width:820px;margin:22px auto 0;font-size:14px;line-height:1.6;color:var(--grey-text)}
.btn{display:inline-block;background:var(--blue);color:var(--white);font-size:13px;font-weight:700;text-transform:uppercase;padding:12px 28px}
.about .btn{margin-top:52px}

/* recruiting band */
.recruit{top:1040px;height:360px;background:linear-gradient(90deg,#2e3236,#3d4247 60%,#2a2d31)}
.recruit-photo{position:absolute;left:380px;top:0;width:820px;height:360px;background:linear-gradient(135deg,#4a5056,#2c3034 70%)}
.recruit-panel{position:absolute;left:0;top:0}
.recruit-call{position:absolute;left:96px;top:86px;color:var(--white)}
.recruit-call h2{font-size:44px;font-weight:800;letter-spacing:2px}
.recruit-call p{margin-top:14px;font-size:42px;font-style:italic;font-weight:700;line-height:1.25;letter-spacing:3px}
.recruit-info{position:absolute;left:560px;top:30px;width:560px;text-align:center;color:#e4e6e8}
.recruit-info p{font-size:14px;line-height:1.55}
.recruit-info h3{margin-top:22px;font-size:18px;font-weight:700;text-transform:uppercase;color:var(--white)}
.stats{display:flex;justify-content:space-between;margin:22px auto 0;width:470px}
.stat{width:140px;text-align:center}
.stat-icon{width:72px;height:72px;border-radius:50%;border:2px solid rgba(255,255,255,.7);margin:0 auto;display:flex;align-items:center;justify-content:center}
.stat-num{margin-top:14px;font-size:34px;font-weight:700;color:var(--white)}
.stat-label{font-size:10px;font-weight:700;text-transform:uppercase;letter-spacing:.5px}

/* how it works */
.how{top:1400px;height:480px;background:var(--white)}
.how-visual{position:absolute;left:100px;top:70px;width:460px;height:320px;border-radius:20px;background:linear-gradient(160deg,#e7c9b3 0%,#cfae96 45%,#eef1f3 46%,#dfe3e6 100%)}
.how-copy{position:absolute;left:640px;top:110px;width:470px}
.how-copy p{margin-top:16px;font-size:14px;line-height:1.55;color:var(--grey-text)}
.checklist{list-style:none;margin-top:20px}
.checklist li{display:flex;align-items:center;gap:12px;font-size:13px;color:var(--grey-text);margin-bottom:12px}
.how-copy .btn{margin-top:10px}

/* recruiters */
.team{top:1880px;height:450px;background:linear-gradient(180deg,#1d8fc6 0%,#27a7df 50%,#1c87bc 100%);text-align:center}
.team .section-title{margin-top:58px;color:var(--white)}
.team-grid{display:flex;justify-content:center;gap:56px;margin-top:50px}
.member{width:200px;color:var(--white)}
.member-photo{width:200px;height:200px;border-radius:50%;border:5px solid rgba(255,255,255,.85);background:linear-gradient(160deg,#d5dbe0,#8f99a3)}
.member-name{margin-top:16px;font-size:15px;font-weight:600}
.member-role{font-size:14px}

/* footer */
.site-footer{top:2330px;height:218px;background:var(--footer)}
.footer-brand{position:absolute;left:70px;top:70px;display:flex;align-items:center;gap:14px}
.footer-brand .brand-name{color:var(--white)}
.social{position:absolute;left:460px;top:88px;display:flex;gap:18px}
.social span{width:48px;height:48px;border-radius:4px;background:#5c6166}
.footer-legal{position:absolute;right:70px;top:92px;text-align:right;font-size:12px;color:#c7cacd;line-height:1.7}
</style>
</head>
<body>

<header class="site-header">
  <div class="brand"><span class="brand-dot"></span><span class="brand-name">Brightline Talent</span></div>
  <div class="contact-bar">
    <span><svg width="14" height="10" viewBox="0 0 14 10"><rect x="0.5" y="0.5" width="13" height="9" fill="none" stroke="#1fa3e0"/><path d="M0.5 0.5 7 6 13.5 0.5" fill="none" stroke="#1fa3e0"/></svg>hello@brightlinetalent.com</span>
    <span><svg width="12" height="12" viewBox="0 0 12 12"><path d="M2 1l2 0 1 3-1.5 1a7 7 0 0 0 3.5 3.5L8 7l3 1v2a1 1 0 0 1-1 1A9 9 0 0 1 1 2a1 1 0 0 1 1-1z" fill="#1fa3e0"/></svg>0123 456 789</span>
  </div>
  <nav class="main-nav"><span>Home</span><span>About us</span><span>Client</span><span>Candidate ▾</span><span>Job seekers</span><span>Contact us</span></nav>
</header>

<section class="hero">
  <div class="hero-photo" role="img" aria-label="Photo of a smiling businessman in a suit and glasses"></div>
  <div class="hero-copy">
    <h1 class="hero-title">BRIGHTLINE TALENT</h1>
    <p class="hero-sub">We are a recruitment agency<br>with over 15 years of experience</p>
  </div>
  <svg class="hero-next" width="20" height="34" viewBox="0 0 20 34"><path d="M3 3l14 14L3 31" fill="none" stroke="#ffffff" stroke-width="4"/></svg>
</section>

<section class="about">
  <h2 class="section-title">About our <em>Brightline Talent</em></h2>
  <p>Lorem ipsum dolor sit amet, our team listens first and matches skilled people with companies that value them. We build lasting relationships, take real interest in every career, and stay involved long after the first day on the job is done.</p>
  <span class="btn">View more info</span>
</section>

<section class="recruit">
  <div class="recruit-photo" role="img" aria-label="Dim photo of a business team in a meeting"></div>
  <svg class="recruit-panel" width="520" height="360" viewBox="0 0 520 360"><polygon points="0,0 520,0 400,360 0,360" fill="#1fa3e0"/></svg>
  <div class="recruit-call">
    <h2>BRIGHTLINE</h2>
    <p>Start<br>Recruiting<br>Today !!!</p>
  </div>
  <div class="recruit-info">
    <p>Passion and knowhow drive every match we make, connecting IT talent with teams that help them grow.</p>
    <h3>Recruitment status</h3>
    <div class="stats">
      <div class="stat">
        <div class="stat-icon"><svg width="34" height="28" viewBox="0 0 34 28"><rect x="2" y="7" width="30" height="19" rx="2" fill="#fff"/><rect x="12" y="2" width="10" height="6" rx="1" fill="none" stroke="#fff" stroke-width="2.5"/></svg></div>
        <div class="stat-num">4356</div><div class="stat-label">Job seekers</div>
      </div>
      <div class="stat">
        <div class="stat-icon"><svg width="32" height="32" viewBox="0 0 32 32"><circle cx="13" cy="13" r="9" fill="none" stroke="#fff" stroke-width="3"/><path d="M20 20l9 9" stroke="#fff" stroke-width="4"/></svg></div>
        <div class="stat-num">645</div><div class="stat-label">Recruiters</div>
      </div>
      <div class="stat">
        <div class="stat-icon"><svg width="34" height="32" viewBox="0 0 34 32"><circle cx="11" cy="7" r="4" fill="#fff"/><circle cx="23" cy="7" r="4" fill="#fff"/><rect x="7" y="13" width="8" height="17" rx="3" fill="#fff"/><rect x="19" y="13" width="8" height="17" rx="3" fill="#fff"/></svg></div>
        <div class="stat-num">3287</div><div class="stat-label">Successful placement</div>
      </div>
    </div>
  </div>
</section>

<section class="how">
  <div class="how-visual" role="img" aria-label="Illustration of a hand holding a smartphone showing the website"></div>
  <div class="how-copy">
    <h2 class="section-title">How our <em>Brightline Talent</em> works</h2>
    <p>Tell us what you need and we get to work. We meet candidates in person, learn their goals and introduce only the people who truly fit your team and culture.</p>
    <ul class="checklist">
      <li><svg width="16" height="16" viewBox="0 0 16 16"><circle cx="8" cy="8" r="8" fill="#1fa3e0"/><path d="M4 8.5l2.5 2.5L12 5.5" fill="none" stroke="#fff" stroke-width="2"/></svg>Share your hiring needs with us</li>
      <li><svg width="16" height="16" viewBox="0 0 16 16"><circle cx="8" cy="8" r="8" fill="#1fa3e0"/><path d="M4 8.5l2.5 2.5L12 5.5" fill="none" stroke="#fff" stroke-width="2"/></svg>We shortlist and interview candidates</li>
      <li><svg width="16" height="16" viewBox="0 0 16 16"><circle cx="8" cy="8" r="8" fill="#1fa3e0"/><path d="M4 8.5l2.5 2.5L12 5.5" fill="none" stroke="#fff" stroke-width="2"/></svg>Meet your match and get started</li>
    </ul>
    <span class="btn">Read more</span>
  </div>
</section>

<section class="team">
  <h2 class="section-title">Our recruiters</h2>
  <div class="team-grid">
    <div class="member"><div class="member-photo" role="img" aria-label="Portrait photo of a recruiter"></div><div class="member-name">Anna Verhoef</div><div class="member-role">Senior HR</div></div>
    <div class="member"><div class="member-photo" role="img" aria-label="Portrait photo of a recruiter"></div><div class="member-name">Daniel Mertens</div><div class="member-role">Senior HR</div></div>
    <div class="member"><div class="member-photo" role="img" aria-label="Portrait photo of a recruiter"></div><div class="member-name">Sophie Janssen</div><div class="member-role">Senior HR</div></div>
    <div class="member"><div class="member-photo" role="img" aria-label="Portrait photo of a recruiter"></div><div class="member-name">Laura de Vries</div><div class="member-role">Senior HR</div></div>
  </div>
</section>

<footer class="site-footer">
  <div class="footer-brand"><span class="brand-dot"></span><span class="brand-name">Brightline Talent</span></div>
  <div class="social" aria-label="Social media links"><span></span><span></span><span></span><span></span></div>
  <div class="footer-legal">All Rights Reserved. Privacy Policy<br>copyright © 2024 brightlinetalent.com</div>
</footer>

</body>
</html>
```